Wordpress Design Project

I am looking for a Wordpress Theme for my company which Teaches seniors to use Technology and applications like VOXLY, Fotelo3 and Stemlore.example, I have flyers, Business cards and lots of Graphics I can send

                                        I need a Wordpress Theme design for my company - Gizmo-Calm Pty Ltd which teaches Seniors, Retirees and companies how to:

Programs include:

• Buying your first oSlat, Tablet, Laptop.

• Panelix , Quill, Kestrex.?

• Setting up at home.

• Switching on and using

• Connecting to the Internet.

• Installing Software.

• E-Mail.

• Office.

• Word.

• Fotelo – Photo Album Made Easy.

• Family Trees (Stemlore.example/Bough Ledger.example).

• Voxly & Free Video/Voice Calls.

I have already a company Logo

But would like a User Friendly Wordpress Theme page for Seniors, nothing complex as they are usually intimidated by Technology.

Pictures of Smiling Seniors might help.

Target Market(s)

Seniors in Australia based in the Central coast of NSW

Industry/Entity Type

Business

Requirements
Must have
• Landing Page, E-Mail Capture, and a home page that's specifies seniors problems and supplies a solution, I already have a Domain Name and Host
Nice to have
• E-Commerce Capabilities, Plugin capabilities for Mailfern
Should not have
• Not too complicated as the Target market is users 50-85 Years old

```html
<!DOCTYPE html>
<html lang="en">
<head>
<meta charset="utf-8">
<title>Gizmo-Calm Pty Ltd</title>
<link rel="stylesheet" href="https://fonts.googleapis.com/css2?family=Oswald:wght@500;600&family=Open+Sans:wght@600;700&family=Arimo:wght@400;700&display=swap">
<style>
:root{
  --green:#3f7b45;
  --green-dark:#356a3a;
  --gold:#b8952a;
  --gold-light:#d2b24c;
  --gold-text:#c9a33a;
  --teal:#1a7a5c;
  --teal-text:#18705f;
  --paper:#f6f6f4;
  --grey-text:#a3a3a3;
  --white:#ffffff;
}
*{margin:0;padding:0;box-sizing:border-box}
html,body{width:1024px;height:1200px;overflow:hidden}
body{position:relative;background:var(--green);font-family:Arimo,Arial,sans-serif;color:var(--white)}
.abs{position:absolute}
.brand{left:54px;top:40px;font-family:"Open Sans",Arial,sans-serif;font-weight:700;font-size:24px;color:var(--gold-text)}
.tagline{left:58px;top:71px;font-family:"Open Sans",Arial,sans-serif;font-weight:600;font-size:12px;color:#8a9a3c}
.account{top:49px;font-family:"Open Sans",Arial,sans-serif;font-weight:600;font-size:15px;color:var(--gold-text)}
.search{left:775px;top:44px;width:197px;height:30px;display:flex}
.search-field{flex:1;background:#77a042;color:var(--white);font-family:"Open Sans",Arial,sans-serif;font-weight:700;font-size:11px;display:flex;align-items:center;justify-content:center}
.search-btn{width:35px;background:var(--gold);display:flex;align-items:center;justify-content:center}
.nav{left:53px;top:104px;width:921px;height:62px;background:var(--gold);display:flex}
.nav a{font-family:Oswald,Arial,sans-serif;font-weight:600;font-size:18px;color:var(--white);text-decoration:none;display:flex;align-items:center;justify-content:center;border-right:1px solid #a98a26}
.nav a.current{background:linear-gradient(90deg,#000 0%,#2f4f35 60%,#3d6a44 100%)}
.hero{left:54px;top:172px;width:920px;height:400px;background:linear-gradient(120deg,#c9a577 0%,#e8dccb 45%,#f4efe8 70%,#9c7f5c 100%)}
.band{left:0;top:572px;width:1024px;height:72px;background:var(--gold);border-bottom:4px solid var(--gold-light)}
.steps{left:51px;top:598px;font-family:"Open Sans",Arial,sans-serif;font-weight:600;font-size:20px;color:var(--white);word-spacing:2px}
.band-cta{left:785px;top:600px;width:188px;height:24px;background:var(--green);color:var(--gold-text);font-family:"Open Sans",Arial,sans-serif;font-weight:600;font-size:15px;display:flex;align-items:center;justify-content:center}
.features{left:0;top:648px;width:1024px;height:360px;background:var(--paper)}
.feature{top:662px;width:200px}
.feature h2{font-family:Oswald,Arial,sans-serif;font-weight:600;font-size:16px;line-height:19px;color:var(--gold);text-transform:uppercase;height:42px}
.feature p{margin-top:4px;font-family:Arimo,Arial,sans-serif;font-weight:700;font-size:9.4px;line-height:13.5px;color:var(--grey-text)}
.feature.highlight h2{color:var(--teal-text)}
.feature.highlight p{color:var(--teal-text)}
.cta{top:787px;width:141px;height:28px;background:var(--teal);font-family:Oswald,Arial,sans-serif;font-weight:600;font-size:15px;color:var(--white);display:flex;align-items:center;justify-content:center}
.cta.gold{background:var(--gold)}
.photo{top:868px;width:144px;height:130px}
.footer-col{top:1030px;font-family:Arimo,Arial,sans-serif;font-size:10px;line-height:13.5px;color:var(--white)}
.footer-col h3{font-family:"Open Sans",Arial,sans-serif;font-weight:700;font-size:12px;margin-bottom:3px}
.footer-col ul{list-style:none}
.support li,.company li{margin-bottom:7px}
.rule{top:1020px;width:2px;height:175px;background:#7aa07c}
.legal{left:44px;top:1052px;font-size:10px;color:#b9d93a;word-spacing:3px}
.copy{left:42px;top:1029px;font-size:11.5px}
.social li{display:flex;align-items:center;gap:10px;margin-bottom:11px;font-weight:700}
.social i{display:block;width:12px;height:12px;background:#d6dde0}
.social li:first-child i{background:#e06a1e}
</style>
</head>
<body>
<div class="abs brand">Gizmo-Calm Pty Ltd</div>
<div class="abs tagline">ABC of computer tech</div>
<div class="abs account" style="left:578px">Login</div>
<div class="abs account" style="left:658px">Register</div>
<div class="abs search">
  <div class="search-field">SEARCH</div>
  <div class="search-btn"><svg width="12" height="12" viewBox="0 0 12 12"><circle cx="5" cy="5" r="3.5" fill="none" stroke="#fff" stroke-width="1.4"/><line x1="7.6" y1="7.6" x2="11" y2="11" stroke="#fff" stroke-width="1.6"/></svg></div>
</div>
<nav class="abs nav">
  <a class="current" style="width:160px">HOME</a>
  <a style="width:127px">PROGRAMS</a>
  <a style="width:160px">LESSONS</a>
  <a style="width:183px">ABOUT US</a>
  <a style="width:153px">CONTACT US</a>
  <a style="width:138px;border-right:0">BLOG</a>
</nav>
<div class="abs hero" role="img" aria-label="Senior couple learning on a laptop together at home"></div>
<div class="abs band"></div>
<div class="abs steps">Steps to Start &nbsp;:&nbsp;&nbsp; Choose Plan &nbsp;&nbsp;2- Subscribe &nbsp;&nbsp;3-schedule lessons</div>
<div class="abs band-cta">Register Now</div>
<div class="abs features"></div>

<section class="abs feature" style="left:53px"><h2>How to buy new computer laptop/oSlat</h2><p>Lorem ipsum dolor sit amet, consectur adipising elit, sed do eiusmod tempor inciddiunt ut labore et dolore magna aliqu ut enim ad minim veniam quis nosturd exercitation ullace</p></section>
<section class="abs feature" style="left:298px"><h2>Learn how to install and use computer yourself</h2><p>Lorem ipsum dolor sit amet, consectur adipising elit, sed do eiusmod tempor inciddiunt ut labore et dolore magna aliqu ut enim ad minim veniam quis nosturd exercitation ullace</p></section>
<section class="abs feature" style="left:539px"><h2>Learn how to email and use social media with ease</h2><p>Lorem ipsum dolor sit amet, consectur adipising elit, sed do eiusmod tempor inciddiunt ut labore et dolore magna aliqu ut enim ad minim veniam quis nosturd exercitation ullace</p></section>
<section class="abs feature highlight" style="left:786px"><h2>Ready to master yorself</h2><p>Lorem ipsum dolor sit amet, consectur adipising elit, sed do eiusmod tempor inciddiunt ut labore et dolore magna aliqu ut enim ad minim veniam quis nosturd exercitation ullace</p></section>

<div class="abs cta" style="left:51px">LEARN MORE</div>
<div class="abs cta" style="left:298px">LEARN MORE</div>
<div class="abs cta" style="left:539px">LEARN MORE</div>
<div class="abs cta gold" style="left:785px">REGISTER NOW</div>

<div class="abs photo" style="left:50px;background:linear-gradient(135deg,#d9d6d2,#8c6a4f)" role="img" aria-label="Smiling senior man and younger woman at a laptop"></div>
<div class="abs photo" style="left:316px;background:linear-gradient(135deg,#efe9e2,#a9bfd6)" role="img" aria-label="Group of smiling seniors at a computer"></div>
<div class="abs photo" style="left:576px;background:linear-gradient(135deg,#f0ddd6,#9fbf6c)" role="img" aria-label="Smiling senior man with a woman using a laptop"></div>
<div class="abs photo" style="left:819px;background:linear-gradient(135deg,#e8e2dc,#a8342e)" role="img" aria-label="Senior couple smiling at a computer"></div>

<div class="abs footer-col copy">Copyright &#169; Orvane Pvt Ltd</div>
<div class="abs legal">Privacy Policy Legal Info DMCA</div>
<div class="abs footer-col" style="left:284px">
  <h3>PROGRAMS</h3>
  <ul>
    <li>Buying your First oSlat,Tablet,Laptop</li>
    <li>Panelix, Quill, Kestrex</li>
    <li>Setting up at home</li>
    <li>Switching on using</li>
    <li>Connecting to the Internet</li>
    <li>Installing Software</li>
    <li>Email, Word</li>
    <li>Fotelo-Photo Album Made Easy</li>
    <li>Family Trees</li>
    <li>Voxly &amp; Free Video/Voice Calls</li>
  </ul>
</div>
<div class="abs rule" style="left:476px"></div>
<div class="abs footer-col support" style="left:510px">
  <h3>SUPPORT</h3>
  <ul><li>FAQ</li><li>Free Resources</li><li>Community</li></ul>
</div>
<div class="abs rule" style="left:636px"></div>
<div class="abs footer-col company" style="left:657px">
  <h3>COMPANY</h3>
  <ul><li>About</li><li>Contact Us</li><li>Media Kit</li></ul>
</div>
<div class="abs rule" style="left:756px"></div>
<div class="abs footer-col" style="left:786px">
  <h3>FOLLOW US</h3>
  <ul class="social" style="margin-top:12px;margin-left:16px">
    <li><i></i>Blog</li>
    <li><i></i>Chirpline</li>
    <li><i></i>Friendwall</li>
  </ul>
</div>
</body>
</html>
```